its a towing company , its called kmr towing and transport. kmr stands for keen mile roadside. on the card looking for colors mainly red with gray and black and white. what the company do. local and long distances ,buy junk cars , snow plow available .tire change ,jumpstart ,and fuel delivery find us on plazabook . kmrtowing@vextramail.com. fax no#732-555-0148 phone no#973-555-0162

Target Market(s)

something that defines keen mile roadside

Contact Information for Business Card

Font styles to use
Decorative

Colors
ef444b
1b1b1b
9d9d9d
ffffff

Requirements
Nice to have
• pics of chains or flatbed dorrin in red
Should not have
• no cartoons

```html
<!DOCTYPE html>
<html lang="en">
<head>
<meta charset="utf-8">
<title>KMR Towing and Transport – Business Card</title>
<link href="https://fonts.googleapis.com/css2?family=Montserrat:wght@600;700;800;900&family=Lato:wght@400;700&display=swap" rel="stylesheet">
<style>
  :root {
    --red: #ef444b;
    --ink: #1b1b1b;
    --gray: #9d9d9d;
    --white: #ffffff;
    --stage: #4a4a4a;
  }
  * { margin: 0; padding: 0; box-sizing: border-box; }
  html, body { width: 1200px; height: 800px; overflow: hidden; }
  body {
    background: var(--stage);
    position: relative;
    font-family: "Lato", sans-serif;
  }
  .card {
    position: absolute;
    width: 630px;
    height: 360px;
    overflow: hidden;
    box-shadow: 0 14px 30px rgba(0,0,0,0.45);
  }
  /* Front side */
  .card-front { left: 80px; top: 30px; }
  .truck-photo {
    position: absolute; inset: 0;
    background: linear-gradient(120deg, #b9bcbf 0%, #a9acae 30%, #c2a3a5 48%, #b0b2b4 62%, #c8cacb 100%);
  }
  .front-brand {
    position: absolute; left: 0; right: 0; top: 98px;
    text-align: center;
  }
  .brand-mark {
    font-family: "Montserrat", sans-serif;
    font-weight: 900;
    color: var(--red);
    letter-spacing: 4px;
    line-height: 1;
  }
  .front-brand .brand-mark { font-size: 70px; }
  .front-brand .brand-tagline {
    font-family: "Montserrat", sans-serif;
    font-weight: 700;
    font-size: 40px;
    color: var(--white);
    margin-top: 4px;
  }
  .service-band {
    position: absolute; left: 0; right: 0; bottom: 0;
    height: 82px;
    background: var(--red);
    color: var(--white);
    font-family: "Montserrat", sans-serif;
    font-weight: 600;
    font-size: 17px;
    text-align: center;
    padding-top: 14px;
    line-height: 27px;
  }
  /* Back side */
  .card-back { left: 490px; top: 410px; background: var(--white); }
  .back-brand { position: absolute; left: 40px; top: 38px; text-align: center; }
  .back-brand .brand-mark { font-size: 64px; }
  .back-brand .brand-tagline {
    font-family: "Montserrat", sans-serif;
    font-weight: 700;
    font-size: 33px;
    color: var(--ink);
    margin-top: 2px;
  }
  .divider {
    position: absolute; left: 40px; right: 40px; top: 178px;
    height: 2px; background: var(--red);
  }
  .person { position: absolute; right: 40px; top: 132px; text-align: right; }
  .person-name { font-family: "Lato", sans-serif; font-weight: 700; font-size: 26px; color: var(--red); }
  .person-role { font-size: 17px; color: var(--ink); margin-top: 10px; }
  .address {
    position: absolute; right: 40px; top: 210px;
    text-align: right; font-size: 18px; line-height: 24px; color: var(--ink);
  }
  .contact-list { position: absolute; left: 48px; top: 198px; list-style: none; }
  .contact-list li {
    display: flex; align-items: center; gap: 12px;
    font-size: 19px; line-height: 27px; color: var(--ink);
  }
  .contact-list svg { width: 16px; height: 16px; fill: var(--red); flex: none; }
  .bottom-edge {
    position: absolute; left: 0; right: 0; bottom: 0; height: 14px; background: var(--red);
  }
</style>
</head>
<body>
  <section class="card card-front" aria-label="Business card front">
    <div class="truck-photo" role="img" aria-label="Photo of a red dorrin flatbed tow truck parked by a road with bare trees"></div>
    <div class="front-brand">
      <div class="brand-mark">KMR</div>
      <div class="brand-tagline">Towing and Transport</div>
    </div>
    <div class="service-band">
      <p>Local and Long distances • Buy junk cars</p>
      <p>Snow plow available • Tire change • Jump start • Fuel delivery</p>
    </div>
  </section>

  <section class="card card-back" aria-label="Business card back">
    <div class="back-brand">
      <div class="brand-mark">KMR</div>
      <div class="brand-tagline">Towing and Transport</div>
    </div>
    <div class="person">
      <div class="person-name">Dale Marrick</div>
      <div class="person-role">Manager</div>
    </div>
    <div class="divider"></div>
    <div class="address">4150 Orin Lane<br>Castell TX 78000</div>
    <ul class="contact-list">
      <li><svg viewBox="0 0 16 16" aria-hidden="true"><path d="M3.5 1l2.5 3-1.5 1.8c.9 2 2.5 3.6 4.5 4.5L10.8 8.8l3.2 2.5-1.5 3C7 14 2 9 1.8 3.3z"/></svg>973-555-0162</li>
      <li><svg viewBox="0 0 16 16" aria-hidden="true"><path d="M4 1h8v4H4zM1 6h14v6h-3v3H4v-3H1zM5 10v4h6v-4z"/></svg>732-555-0148</li>
      <li><svg viewBox="0 0 16 16" aria-hidden="true"><path d="M1 3h14v10H1zM2.5 4.5v.4L8 9l5.5-4.1v-.4z"/></svg>kmrtowing@vextramail.com</li>
      <li><svg viewBox="0 0 16 16" aria-hidden="true"><rect x="2" y="2" width="12" height="12" rx="1"/></svg>/kmrtowing</li>
    </ul>
    <div class="bottom-edge"></div>
  </section>
</body>
</html>
```